Visitenkarten-Design für Psycho-Kinesiologie Praxis
Kavendo Strich Mattis war ein vorzüglicher Grafiker, er hat alle meine vielen Änderungswünsche, kreativ und sehr speditiv umgesetzt, hat eigene Ideen mit eingebracht und einfach tolle Arbeit geleistet, jederzeit sehr zu empfehlen. Viele Grüsse Knut
Zielgruppe
praxis für Psycho-Kinesiologie - Systematische Familienaufstellungen. Einzelsitzungen Gruppentherapie
Ich suche ein Design was auf der einen Seite auffällt, aus dem Rahmen fällt und trotzdem seriös wirkt und Vertrauen schafft.
Die Anhänge sind nur meine Entwürfe also keine fixen Vorgaben
Aufgabenstellung
Eine Seite soll auffallen und Kreativ gestaltet sein
Es gibt ein Template aber die Farben sind noch nicht definiert.
https://www.vorlagenhafen.com/de/demo/48302.html
Es gibt ein Logo (Systemanalytiker) da sind die Farben auch nicht fix Definiert. Gerne sehe ich verschiedene Farbkombinationen
Foto: besseres folgt in kürze
Lend Kindness Circle: Kann auf einer Seite drauf sein, wenn genug Platz,

```html
<!DOCTYPE html>
<html lang="de">
<head>
<meta charset="utf-8">
<title>Visitenkarten Wegklar – Farbvarianten</title>
<link href="https://fonts.googleapis.com/css2?family=Jost:wght@300;400&family=Open+Sans:wght@400;700&display=swap" rel="stylesheet">
<style>
  :root {
    --canvas: #ffffff;
    --card-dark: #2a2d30;
    --panel-grey: #3f4447;
    --brand-red: #a51e2d;
    --text-light: #ffffff;
    --text-dark: #2a2d30;
    --text-soft: #c9cbcd;
  }
  * { box-sizing: border-box; margin: 0; padding: 0; }
  html, body { width: 857px; height: 1200px; overflow: hidden; background: var(--canvas); }
  .sheet { position: relative; width: 857px; height: 1200px; }
  .variant { position: absolute; left: 187px; display: flex; gap: 23px; }
  .card {
    position: relative; width: 233px; height: 150px; overflow: hidden;
    background: var(--card-dark); color: var(--text-light);
    box-shadow: 0 2px 5px rgba(0,0,0,.35);
    font-family: "Jost", sans-serif;
  }
  .card__swirl {
    position: absolute; right: 0; top: 0; width: 130px; height: 139px;
    background: radial-gradient(ellipse at 70% 40%, rgba(165,30,45,.14) 0%, rgba(42,45,48,0) 70%);
  }
  .variant--soft .card__swirl {
    background: radial-gradient(ellipse at 70% 40%, rgba(255,255,255,.05) 0%, rgba(42,45,48,0) 70%);
  }
  .tagline {
    position: absolute; left: 0; right: 0; bottom: 0; height: 11px;
    background: var(--brand-red); color: var(--text-light);
    font-family: "Open Sans", sans-serif; font-size: 6.6px; line-height: 11px;
    text-align: center; white-space: nowrap;
  }
  /* front */
  .front__brand { position: absolute; left: 34px; top: 58px; width: 160px; }
  .wordmark { font-family: "Jost", sans-serif; font-weight: 300; font-size: 34px; line-height: 1; color: var(--text-light); }
  .role { font-size: 6.8px; color: var(--text-soft); text-align: right; margin-top: 2px; }
  .front__name { font-size: 13px; font-weight: 300; text-align: right; margin-top: 2px; }
  /* back */
  .back { display: flex; }
  .back__info { position: relative; width: 116px; height: 139px; padding: 19px 0 0 5px; font-size: 5.4px; line-height: 7.9px; }
  .back__info--light { background: #fff; color: var(--text-dark); }
  .back__info--red { background: var(--brand-red); color: var(--text-light); }
  .back__info--grey { background: var(--panel-grey); color: var(--text-light); }
  .services li { list-style: none; padding-left: 3px; }
  .services li.is-head { border-left: .6px solid var(--brand-red); }
  .back__info--red .services li.is-head,
  .back__info--grey .services li.is-head { border-left-color: var(--text-light); }
  .contact { position: absolute; left: 5px; top: 83px; }
  .contact__row { display: flex; gap: 3px; align-items: flex-start; margin-bottom: 3px; }
  .contact__row svg { width: 5px; height: 5px; flex: none; margin-top: 1.4px; }
  .icon { fill: var(--brand-red); }
  .back__info--red .icon, .back__info--grey .icon { fill: var(--text-light); }
  .back__id { position: relative; flex: 1; height: 139px; padding: 26px 6px 0 6px; }
  .back__brand { position: relative; }
  .back__brand .wordmark { font-size: 21px; }
  .back__brand .role { font-size: 4px; margin-top: 1px; }
  .back__name { position: relative; margin-top: 20px; font-family: "Open Sans", sans-serif; font-size: 7.2px; font-weight: 700; line-height: 8px; }
  .back__name span { display: block; font-weight: 400; font-family: "Jost", sans-serif; font-size: 6.4px; }
  .partner { position: absolute; right: 6px; bottom: 4px; text-align: center; width: 56px; }
  .partner__dot { width: 22px; height: 22px; border-radius: 50%; background: var(--text-light); margin: 0 auto 3px; }
  .partner__name { font-family: "Open Sans", sans-serif; font-size: 5.4px; font-weight: 700; white-space: nowrap; }
</style>
</head>
<body>
<main class="sheet">

  <svg width="0" height="0" style="position:absolute" aria-hidden="true">
    <defs>
      <symbol id="i-phone" viewBox="0 0 10 10"><path d="M2 0.5l2 2-1 1.2c.6 1.4 1.6 2.4 3 3l1.2-1 2 2-1.2 1.6C4 9 1 6 .4 1.7z"/></symbol>
      <symbol id="i-mail" viewBox="0 0 10 10"><path d="M0 2h10v6H0z"/></symbol>
      <symbol id="i-web" viewBox="0 0 10 10"><path d="M5 0a5 5 0 1 0 0 10A5 5 0 0 0 5 0zm-4 4.4h8v1.2H1zM4.4 1h1.2v8H4.4z"/></symbol>
    </defs>
  </svg>

  <section class="variant" style="top:37px">
    <article class="card front"><div class="card__swirl" role="img" aria-label="Dekorativer Schwung im Hintergrund"></div>
      <div class="front__brand"><div class="wordmark">Wegklar</div><div class="role">Systemanalytiker</div><div class="front__name">Knut Haldiger</div></div>
      <div class="tagline">Gesundheit - Glück - Liebe - Frieden - Version Klar - Version Kreativ</div></article>
    <article class="card back">
      <div class="back__info back__info--light">
        <ul class="services"><li class="is-head">Psycho-Kinesiologie</li><li>(nach Dr. Bernholt)</li><li class="is-head">Neurobiologie</li><li class="is-head">Mentalfeldtherapie</li><li class="is-head">Geistiges Familienstellen</li></ul>
        <div class="contact">
          <div class="contact__row"><svg class="icon"><use href="#i-phone"/></svg><div>Schweiz<br>0041 791 204 386</div></div>
          <div class="contact__row"><svg class="icon"><use href="#i-phone"/></svg><div>Deutschland<br>0049 170 482 16 59</div></div>
          <div class="contact__row"><svg class="icon"><use href="#i-mail"/></svg><div>info@wegklar-praxis.ch</div></div>
          <div class="contact__row"><svg class="icon"><use href="#i-web"/></svg><div>www.wegklar-praxis.ch</div></div>
        </div>
      </div>
      <div class="back__id"><div class="card__swirl" role="img" aria-label="Dekorativer Schwung im Hintergrund"></div>
        <div class="back__brand"><div class="wordmark">Wegklar</div><div class="role">Systemanalytiker</div></div>
        <div class="back__name">Knut Haldiger<span>Systemanalytiker</span></div>
        <div class="partner"><div class="partner__dot"></div><div class="partner__name">Lend Kindness Circle</div></div>
      </div>
      <div class="tagline">Gesundheit - Glück - Liebe - Frieden - Version Klar - Version Kreativ</div></article>
  </section>

  <section class="variant variant--soft" style="top:234px">
    <article class="card front"><div class="card__swirl" role="img" aria-label="Dekorativer Schwung im Hintergrund"></div>
      <div class="front__brand"><div class="wordmark">Wegklar</div><div class="role">Systemanalytiker</div><div class="front__name">Knut Haldiger</div></div>
      <div class="tagline">Gesundheit - Glück - Liebe - Frieden - Version Klar - Version Kreativ</div></article>
    <article class="card back">
      <div class="back__info back__info--light">
        <ul class="services"><li class="is-head">Psycho-Kinesiologie</li><li>(nach Dr. Bernholt)</li><li class="is-head">Neurobiologie</li><li class="is-head">Mentalfeldtherapie</li><li class="is-head">Geistiges Familienstellen</li></ul>
        <div class="contact">
          <div class="contact__row"><svg class="icon"><use href="#i-phone"/></svg><div>Schweiz<br>0041 791 204 386</div></div>
          <div class="contact__row"><svg class="icon"><use href="#i-phone"/></svg><div>Deutschland<br>0049 170 482 16 59</div></div>
          <div class="contact__row"><svg class="icon"><use href="#i-mail"/></svg><div>info@wegklar-praxis.ch</div></div>
          <div class="contact__row"><svg class="icon"><use href="#i-web"/></svg><div>www.wegklar-praxis.ch</div></div>
        </div>
      </div>
      <div class="back__id"><div class="card__swirl" role="img" aria-label="Dekorativer Schwung im Hintergrund"></div>
        <div class="back__brand"><div class="wordmark">Wegklar</div><div class="role">Systemanalytiker</div></div>
        <div class="back__name">Knut Haldiger<span>Systemanalytiker</span></div>
        <div class="partner"><div class="partner__dot"></div><div class="partner__name">Lend Kindness Circle</div></div>
      </div>
      <div class="tagline">Gesundheit - Glück - Liebe - Frieden - Version Klar - Version Kreativ</div></article>
  </section>

  <section class="variant" style="top:434px">
    <article class="card front"><div class="card__swirl" role="img" aria-label="Dekorativer Schwung im Hintergrund"></div>
      <div class="front__brand"><div class="wordmark">Wegklar</div><div class="role">Systemanalytiker</div><div class="front__name">Knut Haldiger</div></div>
      <div class="tagline">Gesundheit - Glück - Liebe - Frieden - Version Klar - Version Kreativ</div></article>
    <article class="card back">
      <div class="back__info back__info--red">
        <ul class="services"><li class="is-head">Psycho-Kinesiologie</li><li>(nach Dr. Bernholt)</li><li class="is-head">Neurobiologie</li><li class="is-head">Mentalfeldtherapie</li><li class="is-head">Geistiges Familienstellen</li></ul>
        <div class="contact">
          <div class="contact__row"><svg class="icon"><use href="#i-phone"/></svg><div>Schweiz<br>0041 791 204 386</div></div>
          <div class="contact__row"><svg class="icon"><use href="#i-phone"/></svg><div>Deutschland<br>0049 170 482 16 59</div></div>
          <div class="contact__row"><svg class="icon"><use href="#i-mail"/></svg><div>info@wegklar-praxis.ch</div></div>
          <div class="contact__row"><svg class="icon"><use href="#i-web"/></svg><div>www.wegklar-praxis.ch</div></div>
        </div>
      </div>
      <div class="back__id"><div class="card__swirl" role="img" aria-label="Dekorativer Schwung im Hintergrund"></div>
        <div class="back__brand"><div class="wordmark">Wegklar</div><div class="role">Systemanalytiker</div></div>
        <div class="back__name">Knut Haldiger<span>Systemanalytiker</span></div>
        <div class="partner"><div class="partner__dot"></div><div class="partner__name">Lend Kindness Circle</div></div>
      </div>
      <div class="tagline">Gesundheit - Glück - Liebe - Frieden - Version Klar - Version Kreativ</div></article>
  </section>

  <section class="variant variant--soft" style="top:630px">
    <article class="card front"><div class="card__swirl" role="img" aria-label="Dekorativer Schwung im Hintergrund"></div>
      <div class="front__brand"><div class="wordmark">Wegklar</div><div class="role">Systemanalytiker</div><div class="front__name">Knut Haldiger</div></div>
      <div class="tagline">Gesundheit - Glück - Liebe - Frieden - Version Klar - Version Kreativ</div></article>
    <article class="card back">
      <div class="back__info back__info--red">
        <ul class="services"><li class="is-head">Psycho-Kinesiologie</li><li>(nach Dr. Bernholt)</li><li class="is-head">Neurobiologie</li><li class="is-head">Mentalfeldtherapie</li><li class="is-head">Geistiges Familienstellen</li></ul>
        <div class="contact">
          <div class="contact__row"><svg class="icon"><use href="#i-phone"/></svg><div>Schweiz<br>0041 791 204 386</div></div>
          <div class="contact__row"><svg class="icon"><use href="#i-phone"/></svg><div>Deutschland<br>0049 170 482 16 59</div></div>
          <div class="contact__row"><svg class="icon"><use href="#i-mail"/></svg><div>info@wegklar-praxis.ch</div></div>
          <div class="contact__row"><svg class="icon"><use href="#i-web"/></svg><div>www.wegklar-praxis.ch</div></div>
        </div>
      </div>
      <div class="back__id"><div class="card__swirl" role="img" aria-label="Dekorativer Schwung im Hintergrund"></div>
        <div class="back__brand"><div class="wordmark">Wegklar</div><div class="role">Systemanalytiker</div></div>
        <div class="back__name">Knut Haldiger<span>Systemanalytiker</span></div>
        <div class="partner"><div class="partner__dot"></div><div class="partner__name">Lend Kindness Circle</div></div>
      </div>
      <div class="tagline">Gesundheit - Glück - Liebe - Frieden - Version Klar - Version Kreativ</div></article>
  </section>

  <section class="variant" style="top:827px">
    <article class="card front"><div class="card__swirl" role="img" aria-label="Dekorativer Schwung im Hintergrund"></div>
      <div class="front__brand"><div class="wordmark">Wegklar</div><div class="role">Systemanalytiker</div><div class="front__name">Knut Haldiger</div></div>
      <div class="tagline">Gesundheit - Glück - Liebe - Frieden - Version Klar - Version Kreativ</div></article>
    <article class="card back">
      <div class="back__info back__info--grey">
        <ul class="services"><li class="is-head">Psycho-Kinesiologie</li><li>(nach Dr. Bernholt)</li><li class="is-head">Neurobiologie</li><li class="is-head">Mentalfeldtherapie</li><li class="is-head">Geistiges Familienstellen</li></ul>
        <div class="contact">
          <div class="contact__row"><svg class="icon"><use href="#i-phone"/></svg><div>Schweiz<br>0041 791 204 386</div></div>
          <div class="contact__row"><svg class="icon"><use href="#i-phone"/></svg><div>Deutschland<br>0049 170 482 16 59</div></div>
          <div class="contact__row"><svg class="icon"><use href="#i-mail"/></svg><div>info@wegklar-praxis.ch</div></div>
          <div class="contact__row"><svg class="icon"><use href="#i-web"/></svg><div>www.wegklar-praxis.ch</div></div>
        </div>
      </div>
      <div class="back__id"><div class="card__swirl" role="img" aria-label="Dekorativer Schwung im Hintergrund"></div>
        <div class="back__brand"><div class="wordmark">Wegklar</div><div class="role">Systemanalytiker</div></div>
        <div class="back__name">Knut Haldiger<span>Systemanalytiker</span></div>
        <div class="partner"><div class="partner__dot"></div><div class="partner__name">Lend Kindness Circle</div></div>
      </div>
      <div class="tagline">Gesundheit - Glück - Liebe - Frieden - Version Klar - Version Kreativ</div></article>
  </section>

  <section class="variant variant--soft" style="top:1024px">
    <article class="card front"><div class="card__swirl" role="img" aria-label="Dekorativer Schwung im Hintergrund"></div>
      <div class="front__brand"><div class="wordmark">Wegklar</div><div class="role">Systemanalytiker</div><div class="front__name">Knut Haldiger</div></div>
      <div class="tagline">Gesundheit - Glück - Liebe - Frieden - Version Klar - Version Kreativ</div></article>
    <article class="card back">
      <div class="back__info back__info--grey">
        <ul class="services"><li class="is-head">Psycho-Kinesiologie</li><li>(nach Dr. Bernholt)</li><li class="is-head">Neurobiologie</li><li class="is-head">Mentalfeldtherapie</li><li class="is-head">Geistiges Familienstellen</li></ul>
        <div class="contact">
          <div class="contact__row"><svg class="icon"><use href="#i-phone"/></svg><div>Schweiz<br>0041 791 204 386</div></div>
          <div class="contact__row"><svg class="icon"><use href="#i-phone"/></svg><div>Deutschland<br>0049 170 482 16 59</div></div>
          <div class="contact__row"><svg class="icon"><use href="#i-mail"/></svg><div>info@wegklar-praxis.ch</div></div>
          <div class="contact__row"><svg class="icon"><use href="#i-web"/></svg><div>www.wegklar-praxis.ch</div></div>
        </div>
      </div>
      <div class="back__id"><div class="card__swirl" role="img" aria-label="Dekorativer Schwung im Hintergrund"></div>
        <div class="back__brand"><div class="wordmark">Wegklar</div><div class="role">Systemanalytiker</div></div>
        <div class="back__name">Knut Haldiger<span>Systemanalytiker</span></div>
        <div class="partner"><div class="partner__dot"></div><div class="partner__name">Lend Kindness Circle</div></div>
      </div>
      <div class="tagline">Gesundheit - Glück - Liebe - Frieden - Version Klar - Version Kreativ</div></article>
  </section>

</main>
</body>
</html>
```